Lumora Fabrix
A technical textile company
Lumora Fabrix -
Creative Brief
Professional
Ravi Kapoorji
Business Manager
117, Neel Kamal Residency Chandan Path , Moti Nagar Jaipur - 302049 Rajasthan , India
ravi.kapoorji@lumora-fabrix.example
www.lumora-fabrix.example
Skype : ravikelmora.. Also want - letter head - envelope - power point slide ( both first and regular pages) designs .
Address has to go in the back 117, Neel Kamal Residency Chandan Path , Moti Nagar Jaipur - 302049 Rajasthan , India

```html
<!DOCTYPE html>
<html lang="en">
<head>
<meta charset="utf-8">
<title>Lumora Fabrix Stationery</title>
<link rel="stylesheet" href="https://fonts.googleapis.com/css2?family=Open+Sans:wght@400;600;700&display=swap">
<style>
  :root {
    --bg: #e6e4e1;
    --paper: #ffffff;
    --navy: #1c2d5c;
    --blue: #1e8ccb;
    --orange: #ef7d22;
    --ink: #4a4f5a;
    --muted: #8a8f99;
    --shadow: 0 4px 14px rgba(0,0,0,0.22);
  }
  * { box-sizing: border-box; margin: 0; padding: 0; }
  html, body { width: 1200px; height: 682px; overflow: hidden; }
  body {
    background: var(--bg);
    font-family: "Open Sans", Arial, sans-serif;
    color: var(--ink);
    position: relative;
  }
  .sheet { position: absolute; background: var(--paper); box-shadow: var(--shadow); overflow: hidden; }

  .brand { display: flex; align-items: center; gap: 5px; }
  .brand-mark { width: 10px; height: 10px; background: var(--orange); }
  .brand-name { font-weight: 700; color: var(--navy); letter-spacing: -0.2px; white-space: nowrap; }

  .band { position: absolute; left: 0; right: 0; bottom: 0; }
  .band-blue { background: var(--blue); }
  .band-navy { background: var(--navy); }

  /* Business card front */
  .card-front { left: 96px; top: 60px; width: 276px; height: 168px; }
  .card-front .brand { position: absolute; left: 16px; top: 20px; }
  .card-front .brand-name { font-size: 15px; }
  .card-front .person { position: absolute; left: 16px; top: 64px; }
  .person-name { color: var(--orange); font-size: 10px; font-weight: 700; letter-spacing: 0.6px; text-transform: uppercase; }
  .person-role { font-size: 6px; color: var(--muted); margin-bottom: 7px; }
  .contact-line { font-size: 5.5px; line-height: 1.55; color: var(--ink); }
  .contact-line b { color: var(--orange); font-weight: 600; }
  .card-front .band-blue { height: 16px; }
  .card-front .band-navy { height: 12px; display: flex; align-items: center; justify-content: center; }
  .tagline { color: #fff; font-size: 5.5px; letter-spacing: 2px; text-transform: uppercase; }

  /* Business card back */
  .card-back { left: 389px; top: 60px; width: 288px; height: 168px; }
  .card-back .brand { position: absolute; left: 50%; top: 24px; transform: translateX(-50%); }
  .card-back .brand-name { font-size: 15px; }
  .card-back .address { position: absolute; left: 16px; top: 92px; font-size: 5.5px; line-height: 1.6; }
  .card-back .web { position: absolute; right: 16px; bottom: 16px; font-size: 5.5px; }
  .card-back .band-blue { height: 6px; }

  /* Letterhead */
  .letterhead { left: 700px; top: 66px; width: 424px; height: 536px; }
  .letterhead .brand { position: absolute; left: 24px; top: 28px; }
  .letterhead .brand-name { font-size: 16px; }
  .letterhead .footer { position: absolute; left: 24px; right: 24px; bottom: 22px; font-size: 5.5px; line-height: 1.6; }
  .letterhead .band-blue { height: 5px; bottom: 8px; }
  .letterhead .band-navy { height: 8px; }

  /* Envelope */
  .envelope { left: 100px; top: 396px; width: 380px; height: 198px; }
  .envelope .brand { position: absolute; left: 22px; top: 20px; }
  .envelope .brand-name { font-size: 15px; }
  .envelope .address { position: absolute; left: 22px; top: 108px; font-size: 5.5px; line-height: 1.6; }
  .envelope .band-blue { height: 5px; bottom: 8px; }
  .envelope .band-navy { height: 8px; }

  /* Envelope back with flap */
  .envelope-back { left: 500px; top: 250px; width: 180px; height: 110px; }
  .envelope-back svg { position: absolute; inset: 0; }
  .envelope-back .brand { position: absolute; left: 50%; top: 20px; transform: translateX(-50%); }
  .envelope-back .brand-name { font-size: 9px; }
  .envelope-back .brand-mark { width: 6px; height: 6px; }
</style>
</head>
<body>

  <section class="sheet card-front">
    <div class="brand"><span class="brand-mark"></span><span class="brand-name">Lumora Fabrix</span></div>
    <div class="person">
      <p class="person-name">Ravi Kapoorji</p>
      <p class="person-role">Business Manager</p>
      <p class="contact-line"><b>Cell :</b> +91 90000 12345</p>
      <p class="contact-line"><b>Email :</b> ravi.kapoorji@lumora-fabrix.example</p>
      <p class="contact-line"><b>Skype :</b> ravikelmora..</p>
    </div>
    <div class="band band-blue"></div>
    <div class="band band-navy"><span class="tagline">technical textiles and beyond</span></div>
  </section>

  <section class="sheet card-back">
    <div class="brand"><span class="brand-mark"></span><span class="brand-name">Lumora Fabrix</span></div>
    <address class="address" style="font-style:normal">
      117, Neel Kamal Residency<br>Chandan Path , Moti Nagar<br>Jaipur - 302049<br>Rajasthan , India
    </address>
    <p class="web">www.lumora-fabrix.example</p>
    <div class="band band-blue"></div>
  </section>

  <section class="sheet envelope-back">
    <svg width="180" height="110" viewBox="0 0 180 110" aria-hidden="true">
      <polyline points="0,0 90,58 180,0" fill="none" stroke="#d6d8dc" stroke-width="1"/>
      <rect x="0" y="104" width="180" height="6" fill="#1e8ccb"/>
    </svg>
    <div class="brand"><span class="brand-mark"></span><span class="brand-name">Lumora Fabrix</span></div>
  </section>

  <section class="sheet letterhead">
    <div class="brand"><span class="brand-mark"></span><span class="brand-name">Lumora Fabrix</span></div>
    <div class="footer">
      <p>117, Neel Kamal Residency Chandan Path , Moti Nagar , Jaipur - 302049 , Rajasthan , India</p>
      <p>Cell : +91 90000 12345 &nbsp;|&nbsp; Email : ravi.kapoorji@lumora-fabrix.example</p>
    </div>
    <div class="band band-blue"></div>
    <div class="band band-navy"></div>
  </section>

  <section class="sheet envelope">
    <div class="brand"><span class="brand-mark"></span><span class="brand-name">Lumora Fabrix</span></div>
    <address class="address" style="font-style:normal">
      117, Neel Kamal Residency<br>Chandan Path , Moti Nagar<br>Jaipur - 302049<br>Rajasthan , India
    </address>
    <div class="band band-blue"></div>
    <div class="band band-navy"></div>
  </section>

</body>
</html>
```